Business card for boutique investment firm

Need a business card designed for our boutique investment firm called "BrightLedger Investment Fee Advisors". We help investors achieve lower fees through negotiation on their behalf. We have a logo to work with and a color palette. The card should incorporate our tag line "The power of small changes" and space for relevant details. The look and feel should reflect the logo and our brand personality: Humble, Trustworthy, Friendly

Target Market(s)

High net worth investors who are looking for clarity around how they are being charged by their investment advisor

Industry/Entity Type

Boutique

Requirements
Must have
• Logo
Tag line: The Power of Small Changes
Space for relevant contact details: name, title, phone, email, URL, mailing address

Use these fonts: 'AvantGarde Bk BT' and 'AvantGarde Bk BT Demi'
Use these colors:
Orange = C-0 / M-60 / Y-100 / K-0
Grey = C-0 / M-0 / Y-0 / K-60

```html
<!DOCTYPE html>
<html lang="en">
<head>
<meta charset="utf-8">
<title>BrightLedger Investment Fee Advisors — Business Card</title>
<link rel="stylesheet" href="https://fonts.googleapis.com/css2?family=Questrial&display=swap">
<style>
  :root {
    --orange: #e3701e;
    --grey: #77787b;
    --card: #f2f2f1;
    --backdrop: #e4e1dc;
    --shadow: rgba(60, 50, 40, 0.18);
  }
  * { margin: 0; padding: 0; box-sizing: border-box; }
  html, body {
    width: 1200px;
    height: 900px;
    overflow: hidden;
    background: var(--backdrop);
    font-family: "Questrial", "Century Gothic", sans-serif;
  }
  .canvas {
    position: relative;
    width: 1200px;
    height: 900px;
  }
  .card {
    position: absolute;
    width: 525px;
    height: 300px;
    background: var(--card);
    box-shadow: 0 10px 24px var(--shadow);
    overflow: hidden;
  }

  /* Front side */
  .card-front { left: 90px; top: 140px; }
  .front-disc {
    position: absolute;
    left: -60px;
    top: 20px;
    width: 360px;
    height: 360px;
  }
  .tagline {
    position: absolute;
    right: 40px;
    top: 46px;
    text-align: left;
    color: var(--orange);
    text-transform: uppercase;
  }
  .tagline-lead {
    display: block;
    font-size: 24px;
    letter-spacing: 0.5px;
    line-height: 1;
  }
  .tagline-rest {
    display: block;
    font-size: 11.5px;
    letter-spacing: 0.6px;
    margin-top: 4px;
    padding-left: 22px;
  }
  .tagline-rule {
    display: block;
    width: 150px;
    height: 2px;
    margin-top: 12px;
    margin-left: 22px;
    background: var(--orange);
  }

  /* Back side */
  .card-back { left: 585px; top: 460px; }
  .brand {
    position: absolute;
    left: 34px;
    top: 42px;
    display: flex;
    align-items: center;
    gap: 14px;
  }
  .brand-dot {
    width: 56px;
    height: 56px;
    border-radius: 50%;
    background: var(--orange);
    flex: none;
  }
  .brand-name {
    color: var(--grey);
    font-size: 22px;
    line-height: 1.15;
    letter-spacing: 0.3px;
  }
  .holder {
    position: absolute;
    left: 36px;
    top: 140px;
    display: flex;
    align-items: baseline;
    gap: 12px;
  }
  .holder-name {
    color: var(--grey);
    font-size: 21px;
  }
  .holder-title {
    color: var(--orange);
    font-size: 12px;
    letter-spacing: 0.6px;
    text-transform: uppercase;
  }
  .contact {
    position: absolute;
    left: 36px;
    top: 184px;
    list-style: none;
    color: var(--grey);
    font-size: 13.5px;
    line-height: 1.55;
  }
  .contact-label {
    color: var(--orange);
    margin-right: 6px;
  }
  .contact-divider {
    margin: 0 8px;
  }
  .accent-band {
    position: absolute;
    left: 0;
    right: 0;
    bottom: 18px;
    height: 12px;
    background: var(--orange);
  }
</style>
</head>
<body>
<main class="canvas">

  <section class="card card-front" aria-label="Business card, front">
    <svg class="front-disc" viewBox="0 0 360 360" aria-hidden="true">
      <circle cx="180" cy="180" r="180" fill="var(--orange)"/>
    </svg>
    <p class="tagline">
      <span class="tagline-lead">The Power</span>
      <span class="tagline-rest">of small changes</span>
      <span class="tagline-rule"></span>
    </p>
  </section>

  <section class="card card-back" aria-label="Business card, back">
    <div class="brand">
      <span class="brand-dot" aria-hidden="true"></span>
      <span class="brand-name">BrightLedger<br>Investment Fee Advisors</span>
    </div>

    <p class="holder">
      <span class="holder-name">Elena Marsh</span>
      <span class="holder-title">Manager</span>
    </p>

    <ul class="contact">
      <li><span class="contact-label">T</span>917-555-0148<span class="contact-divider">|</span><span class="contact-label">E</span>elena@brightledger.com</li>
      <li>118 Harbor Street Suite 410, New York NY 10005 USA</li>
      <li>www.brightledger.com</li>
    </ul>

    <div class="accent-band" aria-hidden="true"></div>
  </section>

</main>
</body>
</html>
```